Sale PPC Banner Ad Design Update

We need some Brixel PPC Banner Ad's for our sale altered to include product shots in the background. Attached are some examples that we currently use. We want a similar format/look but with the attached product shots used as the background image. Product image is called "PLXOve Tier 4"

Have also included our logo file as well.

Industry/Entity Type

Brixel

Font styles to use
Sans Serif

Requirements
Must have
• The must-have sizes (up to 150kb):
• • Banner: 468 x 60
• • Large mobile banner 320 x 100
• • Leaderboard: 728 x 90
• • Square: 250 x 250
• • Small square: 200 x 200
• • Large rectangle: 336 x 280
Nice to have
• The nice-to-have sizes:
• • Vertical rectangle: 240 x 400
• • Mobile leaderboard: 320 x 50
• • Inline rectangle: 300 x 250
• • Skyscraper: 120 x 600
• • Wide skyscraper: 160 x 600
• • Half-page: 300 x 600
• • Large leaderboard: 970 x 90
• • Billboard: 970 x 250
• • Portrait: 300 x 1050

```html
<!DOCTYPE html>
<html lang="en">
<head>
<meta charset="utf-8">
<title>Brixel Sale Leaderboard</title>
<link rel="stylesheet" href="https://fonts.googleapis.com/css2?family=Cormorant+Garamond:wght@400;600&family=Montserrat:wght@500&display=swap">
<style>
  :root {
    --brand-white: #ffffff;
    --brand-ink: #1b1a1c;
    --sale-gold: #d9c08a;
    --cta-white: #f4f1ec;
    --photo-deep: #2a1f2c;
    --photo-red: #5a2235;
    --photo-blue: #28324f;
    --photo-gold: #5b4a2a;
    --photo-grey: #6b6770;
  }
  html, body {
    margin: 0;
    padding: 0;
    width: 1200px;
    height: 111px;
    overflow: hidden;
    background: var(--brand-white);
  }
  .banner {
    position: relative;
    width: 1200px;
    height: 111px;
    overflow: hidden;
    display: flex;
  }
  .brand-strip {
    width: 66px;
    height: 111px;
    background: var(--brand-white);
    display: flex;
    align-items: center;
    justify-content: center;
    flex-shrink: 0;
  }
  .brand-name {
    transform: rotate(-90deg);
    font-family: "Cormorant Garamond", serif;
    font-weight: 600;
    font-size: 23px;
    color: var(--brand-ink);
    white-space: nowrap;
    letter-spacing: 0.2px;
  }
  .product-photo {
    position: relative;
    flex: 1;
    height: 111px;
    background:
      linear-gradient(180deg, rgba(20,16,22,0.35) 0%, rgba(20,16,22,0.55) 100%),
      linear-gradient(90deg,
        var(--photo-red) 0%,
        var(--photo-grey) 9%,
        var(--photo-deep) 20%,
        var(--photo-blue) 32%,
        var(--photo-red) 44%,
        var(--photo-gold) 55%,
        var(--photo-deep) 64%,
        var(--photo-grey) 74%,
        var(--photo-red) 84%,
        var(--photo-blue) 100%);
  }
  .sale-copy {
    position: absolute;
    left: 0;
    top: 0;
    width: 1200px;
    height: 111px;
    pointer-events: none;
  }
  .sale-title {
    position: absolute;
    left: 570px;
    top: 20px;
    transform: translateX(-50%);
    margin: 0;
    font-family: "Cormorant Garamond", serif;
    font-weight: 400;
    font-size: 47px;
    line-height: 1;
    letter-spacing: 6px;
    color: var(--sale-gold);
  }
  .shop-now {
    position: absolute;
    left: 572px;
    top: 78px;
    transform: translateX(-50%);
    font-family: "Montserrat", sans-serif;
    font-weight: 500;
    font-size: 14px;
    line-height: 1;
    letter-spacing: 3px;
    color: var(--cta-white);
    text-decoration: none;
    white-space: nowrap;
  }
</style>
</head>
<body>
  <div class="banner">
    <div class="brand-strip">
      <span class="brand-name">Brixel</span>
    </div>
    <div class="product-photo" role="img" aria-label="PLXOve Tier 4 loafers worn with patterned socks, standing on a colourful geometric rug"></div>
    <div class="sale-copy">
      <h1 class="sale-title">SALE</h1>
      <a class="shop-now" href="#">SHOP NOW</a>
    </div>
  </div>
</body>
</html>
```